EverLeafGoods - Stationery, logo provided
Business card, headed paper, comp slip, envelope and A4 folded literature doc wallet
EverLeafGoods - Stationery, logo provided -
Creative Brief
Professional
Mark du Verrand
Les Boulins Rue du Cotil St. Andrews Guernsey GY5 8QT
mark@everleafg.co
www.everleafg.co
The headed paper footer should include the words "Kestrow Limited trading as EverLeafGoods" and possibly on the next line, "Registered in Guernsey - Company No. 71624"
Can be blank or leave to your creativity...

```html
<!DOCTYPE html>
<html lang="en">
<head>
<meta charset="utf-8">
<title>EverLeafGoods – Business Card</title>
<link rel="stylesheet" href="https://fonts.googleapis.com/css2?family=Open+Sans:ital,wght@0,400;0,600;0,700;1,700&display=swap">
<style>
  :root {
    --backdrop: #e6e8ea;
    --card: #ffffff;
    --brand-blue: #1f4fa8;
    --deep-blue: #173f96;
    --leaf-green: #6cbf2a;
    --light-green: #a6d84a;
    --text-grey: #4a4f57;
    --rule: #9aa1ab;
  }
  * { margin: 0; padding: 0; box-sizing: border-box; }
  html, body {
    width: 1200px; height: 780px; overflow: hidden;
    background: var(--backdrop);
    font-family: "Open Sans", Arial, sans-serif;
  }
  .business-card {
    position: absolute; left: 60px; top: 60px;
    width: 1080px; height: 660px;
    background: var(--card);
    border-radius: 40px;
    overflow: hidden;
    box-shadow: 0 6px 22px rgba(0,0,0,0.18);
  }
  .brand {
    position: absolute; left: 90px; top: 70px;
    display: flex; align-items: center; gap: 28px;
  }
  .brand-dot {
    width: 200px; height: 200px; border-radius: 50%;
    background: var(--leaf-green);
  }
  .brand-name {
    font-size: 66px; font-weight: 700; color: var(--brand-blue);
    letter-spacing: -1px;
  }
  .holder {
    position: absolute; right: 620px; top: 340px;
    text-align: right; color: var(--text-grey);
  }
  .holder-name {
    font-size: 30px; font-weight: 700; font-style: italic;
    color: var(--brand-blue); margin-bottom: 26px;
  }
  .holder-address { font-size: 20px; line-height: 1.35; }
  .divider {
    position: absolute; left: 486px; top: 330px;
    width: 2px; height: 160px; background: var(--rule);
  }
  .contact-list {
    position: absolute; left: 510px; top: 326px;
    list-style: none; color: var(--text-grey); font-size: 20px;
  }
  .contact-list li { display: flex; align-items: center; gap: 14px; height: 41px; }
  .contact-list svg { width: 26px; height: 26px; fill: var(--deep-blue); }
  .contact-list .at { width: 26px; text-align: center; font-weight: 700; font-size: 24px; color: var(--deep-blue); }
  .card-wave { position: absolute; left: 0; bottom: 0; width: 1080px; height: 200px; }
  .web-address {
    position: absolute; left: 0; right: 0; bottom: 22px;
    text-align: center; color: #fff; font-size: 22px; font-weight: 600;
  }
</style>
</head>
<body>
  <div class="business-card">
    <div class="brand">
      <div class="brand-dot" aria-hidden="true"></div>
      <div class="brand-name">EverLeafGoods</div>
    </div>

    <div class="holder">
      <div class="holder-name">Mark du Verrand</div>
      <div class="holder-address">Les Boulins, Rue du Cotil<br>St. Andrews, Guernsey, GY5 8QT</div>
    </div>

    <div class="divider"></div>

    <ul class="contact-list">
      <li>
        <svg viewBox="0 0 24 24" aria-label="Phone"><path d="M6.6 10.8a15 15 0 0 0 6.6 6.6l2.2-2.2c.3-.3.7-.4 1-.2 1.1.4 2.3.6 3.6.6.6 0 1 .4 1 1V20c0 .6-.4 1-1 1A17 17 0 0 1 3 4c0-.6.4-1 1-1h3.5c.6 0 1 .4 1 1 0 1.2.2 2.4.6 3.6.1.3 0 .7-.2 1z"/></svg>
        0044 1481 300417
      </li>
      <li>
        <svg viewBox="0 0 24 24" aria-label="Mobile"><path d="M7 1h10a2 2 0 0 1 2 2v18a2 2 0 0 1-2 2H7a2 2 0 0 1-2-2V3a2 2 0 0 1 2-2zm0 3v14h10V4zm5 15.5a1.2 1.2 0 1 0 0 2.4 1.2 1.2 0 0 0 0-2.4z"/></svg>
        0044 7700 582903
      </li>
      <li>
        <svg viewBox="0 0 24 24" aria-label="Fax"><path d="M7 2h10v6H7zM4 9h16a2 2 0 0 1 2 2v8a2 2 0 0 1-2 2H4a2 2 0 0 1-2-2v-8a2 2 0 0 1 2-2zm3 3v2h4v-2zm7 0v2h3v-2zM7 16v2h10v-2z"/></svg>
        0044 1481 390258
      </li>
      <li><span class="at">@</span>mark@everleafg.co</li>
    </ul>

    <svg class="card-wave" viewBox="0 0 1080 200" preserveAspectRatio="none" aria-hidden="true">
      <defs>
        <linearGradient id="greenBand" x1="0" x2="1">
          <stop offset="0" stop-color="var(--light-green)"/>
          <stop offset="1" stop-color="var(--leaf-green)"/>
        </linearGradient>
        <linearGradient id="blueBand" x1="0" x2="1">
          <stop offset="0" stop-color="#2a63c4"/>
          <stop offset="1" stop-color="var(--deep-blue)"/>
        </linearGradient>
      </defs>
      <path d="M0 120 C 320 175 700 110 1080 10 L1080 200 L0 200 Z" fill="url(#greenBand)"/>
      <path d="M0 140 C 330 190 720 130 1080 40 L1080 200 L0 200 Z" fill="url(#blueBand)"/>
    </svg>
    <div class="web-address">www.everleafg.co</div>
  </div>
</body>
</html>
```